Flyer-Design für Praxis für Ganzheitliche Gesundheit
Zielgruppe
Ich habe eine Praxis für Ganzheitliche Gesundheit mit den Schwerpunkten systemische Beratung/systemische Aufstellungen und energetisch-geistige Methoden.
Ich möchte mich im Ort und Umgebung als Ergänzung zu den Schulmedizinern etablieren.
Mein Zielpublikum sind Frauen mittleren Alters, deren Beschwerden sich durch die Schulmedizin nicht ausreichend gebessert haben oder die allgemein offen sind für alternative Behandlungsmethoden.
Aufgabenstellung
FORMAT: Din lang plus (10,5 x 21 cm), hochkant, beidseitig bedruckt
Das soll der Flyer ausdrücken:
* Willkommen heißen, Sehnsucht wecken, das Gefühl geben, bei mir gut aufgehoben zu sein, ich kann ihm gut helfen
* dem Klienten Sicherheit, Vertraulichkeit und Geborgenheit vermitteln
* mich darstellen: Seriosität, Tiefe, Freude am Tun, Freundlichkeit
* Optimismus, dass das Ziel erreicht wird
* Klarheit, was er bei mir bekommt (Beratung und Behandlung in den genannten Fällen mit der Aussicht auf das genannte Ziel)
* WICHTIG ist zu beachten, dass der Flyer keine Heilversprechen vermittelt!
FARBEN:
* Elemente in Gelbtönen (weiß – hellgelb – sonnengelb – Gold-Orange; freundlich, aber nicht knallig)
* Schriften bevorzugt in Grautönen
* evtl. Nachtblau/tiefes Dunkelblau als Hintergrund (soll Vertrauenswürdigkeit und Sicherheit ausstrahlen)
* evtl. ein tiefes Dunkelrot für Akzente (nicht als Hintergrund)
* gerne ein komplett farbiger Flyer statt weißem Hintergrund
TEXTE und GESTALTUNGSIDEEN:
VORDERSEITE:
„Karin Lohmeyer“ + „Ganzheitliche Gesundheit“ oder „Praxis für Ganzheitliche Gesundheit“
eventuell, wenn genug Platz: „effektiv, einfühlsam, ergebnisorientiert“
„Ängste, Depressionen, chronische Erkrankungen, schwierige Beziehungen“ (als Ausgangspunkt für den Klienten)
„Impulse für Wohlbefinden, Gesundheit, erfüllte Beziehungen“ (als Ziel, das erreicht wird)
LAYOUTIDEE:
Es soll für den Leser/Klienten ein Weg oder eine Entwicklung sichtbar werden: ausgehend von seinen Problemen über meine Praxis bzw. meine Behandlung/Beratung soll er sein Ziel erreichen.
RÜCKSEITE:
OBERER BEREICH:
3 große Schlagworte für meine Fähigkeiten:
„Kompetenz, Erfahrung, Intuition“
für die Schlagworte Erläuterungen in kleinerer Schrift:
zu Kompetenz: „Biologin, Heilpraktikerin“
zu Erfahrung: ..

```html
<!DOCTYPE html>
<html lang="de">
<head>
<meta charset="utf-8">
<title>Karin Lohmeyer – Ganzheitliche Gesundheit</title>
<link rel="stylesheet" href="https://fonts.googleapis.com/css2?family=Poiret+One&display=swap">
<style>
  :root {
    --sun-yellow: #efbb52;
    --night-blue: #50738f;
    --deep-blue: #3e5d76;
    --cream: #f4e8c6;
    --poppy-red: #ee3a27;
  }
  * { margin: 0; padding: 0; box-sizing: border-box; }
  html, body { width: 1200px; height: 2400px; overflow: hidden; }
  body { background: var(--sun-yellow); font-family: "Poiret One", sans-serif; }
  .flyer { position: relative; width: 1200px; height: 2400px; overflow: hidden; }
  .backdrop { position: absolute; inset: 0; }

  .brand { position: absolute; left: 300px; top: 390px; color: var(--sun-yellow); }
  .brand-name { font-size: 142px; font-weight: 400; line-height: 1; letter-spacing: 1px; }
  .brand-tagline { font-size: 60px; font-weight: 400; margin-top: 18px; margin-left: 6px; color: var(--cream); }

  .panel {
    position: absolute;
    background: var(--night-blue);
    border-radius: 40px;
    box-shadow: 0 -14px 40px rgba(40, 64, 86, 0.55), 0 14px 30px rgba(40, 64, 86, 0.35);
    display: flex; flex-direction: column; justify-content: center; align-items: center;
    color: var(--cream); text-align: center;
  }
  .panel p { font-size: 60px; line-height: 78px; }
  .panel-problems { left: 77px; top: 803px; width: 833px; height: 640px; padding-bottom: 120px; }
  .panel-goals { left: 312px; top: 1495px; width: 818px; height: 625px; }

  .illustration {
    position: absolute; border-radius: 120px;
    background: linear-gradient(160deg, rgba(238, 58, 39, 0.85) 0%, rgba(238, 58, 39, 0.45) 35%, rgba(239, 187, 82, 0.35) 70%, rgba(239, 187, 82, 0.15) 100%);
  }
  .poppy-top { left: 48px; top: 145px; width: 325px; height: 658px; }
  .poppy-right { left: 847px; top: 948px; width: 237px; height: 547px; }
  .poppy-low { left: 44px; top: 1195px; width: 421px; height: 508px;
    background: linear-gradient(20deg, rgba(238, 58, 39, 0.85) 0%, rgba(238, 58, 39, 0.4) 35%, rgba(239, 187, 82, 0.3) 75%, rgba(239, 187, 82, 0.1) 100%); }

  .values {
    position: absolute; left: 0; width: 1200px; top: 2270px;
    text-align: center; font-size: 64px; color: var(--night-blue); letter-spacing: 0.5px;
  }
</style>
</head>
<body>
<main class="flyer">
  <svg class="backdrop" width="1200" height="2400" viewBox="0 0 1200 2400" aria-hidden="true">
    <path d="M0 110 C260 40 560 70 800 140 C980 190 1100 190 1200 183 L1200 2150 C1000 2180 800 2230 600 2222 C380 2214 180 2160 0 2140 Z" fill="var(--deep-blue)" opacity="0.6"/>
    <path d="M0 100 C260 30 560 60 800 130 C980 180 1100 180 1200 175 L1200 2132 C1000 2160 800 2215 600 2208 C380 2200 180 2150 0 2130 Z" fill="var(--night-blue)"/>
  </svg>

  <div class="illustration poppy-top" role="img" aria-label="Gezeichnete rote Mohnblume mit goldenem Stiel und Knospe"></div>

  <header class="brand">
    <h1 class="brand-name">Karin Lohmeyer</h1>
    <p class="brand-tagline">Ganzheitliche Gesundheit</p>
  </header>

  <section class="panel panel-problems">
    <p>Ängste<br>Depressionen<br>chronische Erkrankungen<br>schwierige Beziehungen</p>
  </section>

  <section class="panel panel-goals">
    <p>Impulse für Wohlbefinden<br>Gesundheit<br>erfüllte Beziehungen</p>
  </section>

  <div class="illustration poppy-right" role="img" aria-label="Gezeichnete rote Mohnblume mit langem goldenem Stiel"></div>
  <div class="illustration poppy-low" role="img" aria-label="Hängende rote Mohnblume mit geschwungenem Stiel und Knospe"></div>

  <p class="values">Effektiv • Einfühlsam • Ergebnisorientiert</p>
</main>
</body>
</html>
```